buseisness card

design a card that similar to my web site
BRIXENTAPLORLLC .COM

Contact Information for Business Card

NAME PHONE # WEBSITE EMAIL AND DISCTIPTION OF WHAT WE DO

Colors
0054AA
0677BA
7BADD7
CADEEF
E8F1F8

Requirements
Must have
• lOGO AND DETAILS
Nice to have
• I LIKE THE WATER LIKE ON MY WEB SITE

```html
<!DOCTYPE html>
<html lang="en">
<head>
<meta charset="utf-8">
<title>Brixentaplor – Business Card</title>
<link rel="stylesheet" href="https://fonts.googleapis.com/css2?family=Montserrat:ital,wght@0,400;0,600;0,700;0,800;1,900&display=swap">
<style>
  :root {
    --brand-blue: #24aaec;
    --ink: #1d1d1f;
    --paper: #ffffff;
    --frame: #000000;
    --card-edge: #5a5a5a;
  }
  * { margin: 0; padding: 0; box-sizing: border-box; }
  html, body { width: 1200px; height: 865px; overflow: hidden; background: var(--paper); }
  body { font-family: "Montserrat", sans-serif; color: var(--ink); }

  .sheet {
    position: relative;
    width: 1200px; height: 865px;
    border: 1.5px solid var(--frame);
    background: var(--paper);
  }
  .sheet-title {
    position: absolute; left: 0; right: 0; top: 96px;
    text-align: center;
    font-weight: 900; font-style: italic;
    font-size: 60px; letter-spacing: -2px; line-height: 1;
    color: #000;
  }

  .card {
    position: absolute;
    width: 466px; height: 253px;
    border: 1px solid var(--card-edge);
    border-radius: 4px;
    background: var(--paper);
    overflow: hidden;
  }
  .card--front-light { left: 115px; top: 209px; }
  .card--front-blue  { left: 618px; top: 209px; background: var(--brand-blue); border-color: var(--brand-blue); }
  .card--back-full   { left: 115px; top: 500px; }
  .card--back-short  { left: 618px; top: 500px; }

  .brand-dot { position: absolute; border-radius: 50%; background: var(--brand-blue); }
  .card--front-blue .brand-dot { background: var(--paper); }

  .brand-name {
    position: absolute;
    font-weight: 800; font-size: 23px; line-height: 1;
    color: var(--brand-blue); letter-spacing: 0.2px;
  }
  .card--front-blue .brand-name { color: var(--paper); }

  .tagline { position: absolute; font-size: 11.5px; line-height: 11.5px; font-weight: 400; }
  .tagline strong { font-weight: 600; }

  .person-name {
    position: absolute; left: 41px; top: 52px;
    font-weight: 800; font-size: 23px; line-height: 1;
    color: var(--brand-blue);
  }
  .person-role {
    position: absolute; left: 41px; top: 76px;
    font-weight: 700; font-size: 13px; line-height: 1;
  }
  .direct-line {
    position: absolute; left: 41px;
    font-weight: 600; font-size: 12.5px; line-height: 14.5px;
  }
  .office-info {
    position: absolute;
    font-size: 11.5px; line-height: 13px;
  }
  .card--back-full .office-info { left: 267px; top: 138px; font-weight: 600; }
  .card--back-short .office-info { right: 43px; top: 78px; text-align: right; font-weight: 400; }
</style>
</head>
<body>
<main class="sheet">
  <h1 class="sheet-title">business card</h1>

  <section class="card card--front-light">
    <span class="brand-dot" style="left:97px; top:99px; width:44px; height:44px;"></span>
    <p class="brand-name" style="left:157px; top:116px;">BRIXENTAPLOR</p>
    <p class="tagline" style="left:157px; top:153px;">We develop <strong>methods for annual foam<br>proportioning test</strong></p>
  </section>

  <section class="card card--front-blue">
    <span class="brand-dot" style="left:85px; top:92px; width:68px; height:68px;"></span>
    <p class="brand-name" style="left:170px; top:116px;">BRIXENTAPLOR</p>
  </section>

  <section class="card card--back-full">
    <span class="brand-dot" style="left:381px; top:42px; width:44px; height:44px;"></span>
    <p class="person-name">Lenard Vossberg</p>
    <p class="person-role">Chief Financial Officer</p>
    <p class="direct-line" style="top:106px;">+740 555 0147<br>vossberg@brx204.com</p>
    <p class="tagline" style="left:41px; top:183px;">We develop methods for annual<br>foam proportioning test</p>
    <p class="office-info">info@brx204.com<br>+740 555 0147<br>1180 Harborline Drive<br>Dayton, OH 45402<br>www.brixentaplorllc.com</p>
  </section>

  <section class="card card--back-short">
    <span class="brand-dot" style="left:40px; top:184px; width:92px; height:92px;"></span>
    <p class="person-name">Lenard Vossberg</p>
    <p class="person-role">CFO</p>
    <p class="direct-line" style="top:116px;">+740 555 0147<br>vossberg@brx204.com</p>
    <p class="office-info">info@brx204.com<br>+740 555 0147<br>1180 Harborline Drive<br>Dayton, OH 45402<br>www.brixentaplorllc.com</p>
    <p class="tagline" style="right:43px; top:183px; text-align:right;">We develop methods for annual<br>foam proportioning test</p>
  </section>
</main>
</body>
</html>
```